Morvela Aesthetic Doctor

I require an elegant, luxurious looking business card for my aesthetic business. I am a doctor and that will set me aside from competitors. I am planning to provide home and spa based treatments to clients with high expectations. I have attached my logo.

```html
<!DOCTYPE html>
<html lang="en">
<head>
<meta charset="utf-8">
<title>Morvela Aesthetic Doctor – Business Card</title>
<link href="https://fonts.googleapis.com/css2?family=Poppins:wght@400;500;600&family=Cormorant+Garamond:ital,wght@1,500&display=swap" rel="stylesheet">
<style>
  :root {
    --backdrop: #2b2b2d;
    --blue-light: #2aa9e2;
    --blue-deep: #2b6fc6;
    --blue-dark: #2366b8;
    --blue-mid: #7cc4ea;
    --blue-pale: #b9e1f5;
    --ink-blue: #2a6fc4;
    --grey: #9a9ea6;
    --white: #ffffff;
  }
  * { box-sizing: border-box; margin: 0; padding: 0; }
  html, body { width: 1200px; height: 960px; overflow: hidden; }
  body {
    background: var(--backdrop);
    position: relative;
    font-family: "Poppins", sans-serif;
  }
  .card {
    position: absolute;
    width: 600px;
    height: 343px;
    border-radius: 22px;
    overflow: hidden;
    box-shadow: 0 14px 30px rgba(0,0,0,.45);
  }

  /* Front */
  .card-front {
    left: 90px; top: 110px;
    background: linear-gradient(160deg, var(--blue-light) 0%, var(--blue-deep) 100%);
    color: var(--white);
  }
  .card-front .soft-waves { position: absolute; inset: 0; }
  .front-brand {
    position: absolute; left: 0; right: 0; top: 100px;
    display: flex; align-items: center; justify-content: center; gap: 16px;
  }
  .brand-dot {
    width: 62px; height: 62px; border-radius: 50%;
    border: 3px solid var(--white);
    flex: none;
  }
  .brand-name {
    font-weight: 500; font-size: 34px; line-height: 1.05;
    letter-spacing: 1px; text-transform: uppercase;
  }
  .brand-name small { display: block; font-size: 16px; letter-spacing: 3px; font-weight: 500; }
  .services {
    position: absolute; left: 0; right: 0; bottom: 44px;
    text-align: center; font-size: 14.5px; line-height: 1.6;
  }

  /* Back */
  .card-back {
    left: 510px; top: 500px;
    background: var(--white);
  }
  .card-back .wave-bands { position: absolute; inset: 0; }
  .back-brand {
    position: absolute; left: 34px; top: 92px;
    display: flex; align-items: center; gap: 12px;
    color: var(--ink-blue);
  }
  .back-brand .brand-dot { width: 52px; height: 52px; border-color: var(--grey); }
  .back-brand .brand-name { font-size: 28px; }
  .back-brand .brand-name small { font-size: 13px; }
  .doctor {
    position: absolute; right: 26px; top: 30px; text-align: right;
  }
  .doctor-name { color: var(--ink-blue); font-weight: 600; font-size: 17px; }
  .doctor-title { color: var(--grey); font-size: 11.5px; }
  .tagline {
    position: absolute; left: 36px; top: 200px;
    font-family: "Cormorant Garamond", serif; font-style: italic; font-weight: 500;
    font-size: 22px; color: var(--ink-blue);
  }
  .contacts {
    position: absolute; right: 24px; top: 178px;
    list-style: none; text-align: right;
    color: var(--ink-blue); font-size: 12.5px; font-weight: 500;
  }
  .contacts li {
    display: flex; align-items: center; justify-content: flex-end; gap: 7px;
    height: 24px;
  }
  .icon {
    width: 17px; height: 17px; border-radius: 50%;
    background: var(--blue-light);
    display: inline-flex; align-items: center; justify-content: center;
    flex: none;
  }
  .icon svg { width: 10px; height: 10px; }
</style>
</head>
<body>

<section class="card card-front" aria-label="Card front">
  <svg class="soft-waves" viewBox="0 0 600 343" preserveAspectRatio="none" aria-hidden="true">
    <path d="M0,120 C180,60 360,200 600,110 L600,0 L0,0 Z" fill="#ffffff" opacity=".06"/>
    <path d="M0,260 C200,190 380,320 600,230 L600,343 L0,343 Z" fill="#1f5fb4" opacity=".18"/>
  </svg>
  <div class="front-brand">
    <span class="brand-dot"></span>
    <p class="brand-name">Morvela<small>Aesthetic Doctor</small></p>
  </div>
  <p class="services">
    Dermal injectables • Plasma facials • Microneedling<br>
    Skin boosters • Excessive sweating • Home and Spa Based Treatments
  </p>
</section>

<section class="card card-back" aria-label="Card back">
  <svg class="wave-bands" viewBox="0 0 600 343" preserveAspectRatio="none" aria-hidden="true">
    <path d="M-20,322 C200,326 290,314 335,225 S395,118 630,112" fill="none" stroke="var(--blue-pale)" stroke-width="44"/>
    <path d="M-20,302 C200,306 280,296 322,210 S380,98 630,92" fill="none" stroke="var(--blue-mid)" stroke-width="20"/>
    <path d="M-20,318 C205,322 300,310 345,220 S405,112 630,104" fill="none" stroke="var(--blue-dark)" stroke-width="18"/>
    <path d="M-20,342 C210,346 312,334 358,240 S418,130 630,126" fill="none" stroke="var(--blue-mid)" stroke-width="7"/>
  </svg>

  <div class="doctor">
    <p class="doctor-name">Dr Elise Varnak MRCPCH MD</p>
    <p class="doctor-title">Australasian Diploma of Aesthetic Medicine</p>
  </div>

  <div class="back-brand">
    <span class="brand-dot"></span>
    <p class="brand-name">Morvela<small>Aesthetic Doctor</small></p>
  </div>

  <p class="tagline">Home and Spa Based Treatments</p>

  <ul class="contacts">
    <li>0800 555 019
      <span class="icon"><svg viewBox="0 0 10 10"><path d="M2,1 L4,1 L4.6,3 L3.5,3.8 C4,5 5,6 6.2,6.5 L7,5.4 L9,6 L9,8 C5,8.5 1.5,5 2,1 Z" fill="#fff"/></svg></span></li>
    <li>elise@morvela.co.nz
      <span class="icon"><svg viewBox="0 0 10 10"><rect x="1" y="2.5" width="8" height="5.5" fill="#fff"/><path d="M1,2.5 L5,5.5 L9,2.5" fill="none" stroke="#2aa9e2" stroke-width=".8"/></svg></span></li>
    <li>www.morvela.co.nz
      <span class="icon"><svg viewBox="0 0 10 10"><circle cx="5" cy="5" r="3.8" fill="none" stroke="#fff" stroke-width=".9"/><path d="M1.2,5 H8.8 M5,1.2 V8.8" stroke="#fff" stroke-width=".8"/></svg></span></li>
    <li>Find Us On
      <span class="icon"></span><span class="icon"></span></li>
  </ul>
</section>

</body>
</html>
```